Coffee, Bar , Bakery, Wine Bar, Business based in Fort Lauderdale FL.
We need Logo Design Website (PC and Mobile) design with order and pickup online managment service. Cold Colors Main Images will be glass or bottle of wine and coffee related images
I Attach a logo we found online and we like something like that.

Industry/Entity Type

Business

Logo Text

MERIDO Coffee & Food Co

Number of Pages Required

4 page

Requirements
Must have
• Order online for in store pickup. MENU PAGE !!
Nice to have
• Map with address , link to all social , option to add daily pictures in a slide.
Should not have
• not many white spaces on the web page.

```html
<!DOCTYPE html>
<html lang="en">
<head>
<meta charset="utf-8">
<title>Merido Coffee &amp; Food Co</title>
<link href="https://fonts.googleapis.com/css2?family=Open+Sans:wght@300;400;600;700&family=Roboto+Condensed:wght@400;700&display=swap" rel="stylesheet">
<style>
:root{
  --stage:#4a4a4a;
  --ink:#1c1c1c;
  --black:#000;
  --white:#fff;
  --orange:#e47b0c;
  --beige:#efe6da;
  --muted:#6b6b6b;
  --rule:#cfc6ba;
}
*{margin:0;padding:0;box-sizing:border-box}
html,body{width:1200px;height:1200px;overflow:hidden;background:var(--stage)}
body{font-family:"Open Sans",sans-serif;color:var(--ink)}
.page{position:absolute;left:380px;top:0;width:550px;height:1500px;transform:scale(.8);transform-origin:0 0;background:var(--white);overflow:hidden}
.abs{position:absolute}
.cond{font-family:"Roboto Condensed",sans-serif}

/* header */
.site-header{left:0;top:0;width:550px;height:50px;background:var(--black)}
.nav-link{top:29px;font-size:6.5px;font-weight:700;color:var(--white);letter-spacing:.2px}
.util{top:9px;font-size:6px;font-style:italic;color:#bbb;font-family:Georgia,serif}
.logo-box{left:240px;top:0;width:72px;height:50px;background:var(--white);display:flex;align-items:center;justify-content:center}
.logo-box span{font-family:"Open Sans",sans-serif;font-weight:700;font-size:13px;color:var(--black)}
.btn-top{left:452px;top:7px;width:54px;height:12px;border-radius:6px;background:var(--orange);color:var(--white);font-size:5.5px;font-weight:700;display:flex;align-items:center;justify-content:center}

/* hero */
.hero{left:0;top:50px;width:550px;height:214px;background:linear-gradient(90deg,#5a3a22 0%,#2b1c14 35%,#3b2a22 55%,#6b1b1a 80%,#2a1410 100%)}
.hero-dot{top:232px;width:6px;height:6px;border-radius:50%}
.arrow{top:140px;width:8px;height:26px}

/* welcome */
.welcome-title{left:60px;top:316px;width:195px;text-align:center;font-size:14px;font-weight:700}
.welcome-rule{left:60px;top:351px;width:195px;height:1px;background:#bdbdbd}
.welcome-text{left:40px;width:232px;text-align:center;font-size:5.2px;line-height:10.5px;color:var(--muted)}
.welcome-photo{left:363px;top:318px;width:144px;height:145px;background:linear-gradient(160deg,#a9b783 0%,#6f7f3c 45%,#2c2418 100%)}
.welcome-photo::after{content:"";position:absolute;left:7px;top:7px;right:7px;bottom:7px;border:1px solid rgba(255,255,255,.85)}

/* banner */
.banner{left:0;top:485px;width:550px;height:223px;background:radial-gradient(ellipse at 70% 40%,#6a4526 0%,#3a2416 55%,#22150d 100%)}
.banner-text{left:101px;top:553px;font-size:20px;font-weight:300;color:var(--white);line-height:28px;letter-spacing:.3px}
.btn-order{left:101px;top:624px;width:91px;height:23px;border-radius:12px;background:var(--orange);color:var(--white);font-size:9px;font-weight:700;display:flex;align-items:center;justify-content:center}

/* menu tabs */
.tab{top:748px;font-size:9px;font-weight:700;color:#555}
.tab-active{left:43px;top:743px;width:63px;height:21px;border-radius:6px;background:var(--orange);color:var(--white);display:flex;align-items:center;justify-content:center;font-size:9px;font-weight:700}
.card{top:790px;width:135px;height:172px;border:1px solid #8a8a8a;background:var(--white)}
.card-photo{position:absolute;left:14px;top:12px;width:105px;height:120px;border-radius:4px}
.card-name{position:absolute;left:8px;top:147px;font-size:8.5px;color:#222}
.card-price{position:absolute;right:8px;top:147px;font-size:8.5px;color:var(--orange)}

/* video */
.video-band{left:0;top:997px;width:550px;height:158px;background:var(--beige)}
.video-title{left:43px;top:1027px;width:125px;font-size:6px;font-weight:700;line-height:10.5px;text-transform:uppercase}
.video-text{left:43px;top:1055px;width:128px;font-size:5.2px;line-height:10.5px;color:var(--muted)}
.video-photo{left:180px;top:1020px;width:135px;height:85px;border-radius:40%;background:radial-gradient(ellipse,#d9a35e 0%,#b0702f 60%,rgba(176,112,47,0) 100%)}
.video-reflect{left:180px;top:1105px;width:135px;height:40px;background:linear-gradient(#e6d6c2,rgba(239,230,218,0))}
.thumb{top:1018px;width:83px;height:45px;background:linear-gradient(135deg,#6b4a35,#2a1a12)}
.thumb-title{position:absolute;left:6px;top:4px;font-size:6.5px;color:var(--white)}
.play{position:absolute;left:34px;top:17px;width:15px;height:11px;border-radius:3px;background:rgba(0,0,0,.7)}
.play::after{content:"";position:absolute;left:6px;top:3px;border-left:4px solid #fff;border-top:2.5px solid transparent;border-bottom:2.5px solid transparent}
.thumb-cap{top:1072px;width:90px;font-size:4.6px;font-weight:700;line-height:6.5px;text-transform:uppercase}

/* kit */
.kit-photo{left:67px;top:1192px;width:175px;height:93px;background:linear-gradient(135deg,#7a6552 0%,#3f6f88 45%,#c9b8a4 100%)}
.kit-title{left:282px;top:1191px;font-size:8.5px;font-weight:700}
.kit-list{left:282px;top:1207px;list-style:none}
.kit-list li{font-size:5.2px;line-height:10.6px;color:var(--muted);padding-left:8px;position:relative}
.kit-list li::before{content:"";position:absolute;left:0;top:3.5px;width:4px;height:4px;border-radius:50%;border:1px solid var(--orange)}
.kit-quote{left:0;top:1298px;width:550px;text-align:center;font-size:5.8px;font-weight:700}

/* footer */
.site-footer{left:0;top:1332px;width:550px;height:168px;background:var(--beige)}
.foot-head{top:1355px;width:108px;font-size:8px;font-weight:700;padding-bottom:4px;border-bottom:1px solid var(--rule)}
.foot-text{font-size:5.2px;line-height:9px;color:var(--muted)}
.contact-row{left:43px;display:flex;align-items:flex-start;gap:5px}
.field{left:282px;width:106px;height:11px;border:1px solid var(--rule);background:#f6f0e8;font-size:5px;color:#aaa;padding-left:3px;line-height:9px}
.btn-sub{left:282px;top:1442px;width:46px;height:13px;background:var(--black);color:var(--white);font-size:5px;display:flex;align-items:center;justify-content:center}
.social{top:1398px;width:12px;height:12px;background:var(--white)}
.copy-rule{left:0;top:1473px;width:550px;height:1px;background:var(--rule)}
.copyright{left:0;top:1482px;width:550px;text-align:center;font-size:5.5px}
</style>
</head>
<body>
<div class="page">

  <header class="site-header abs"></header>
  <div class="util abs" style="left:128px">Find / Contacts</div>
  <div class="util abs" style="left:369px">Login / Register</div>
  <div class="btn-top abs">ORDER NAW</div>
  <nav>
    <span class="nav-link abs" style="left:43px">HOME</span>
    <span class="nav-link abs" style="left:95px">ABOUT</span>
    <span class="nav-link abs" style="left:148px">BAR</span>
    <span class="nav-link abs" style="left:192px">BAKERY</span>
    <span class="nav-link abs" style="left:331px;top:30px">BLOG</span>
    <span class="nav-link abs" style="left:374px;top:30px">WINE BAR</span>
    <span class="nav-link abs" style="left:430px;top:30px">COFFEE</span>
    <span class="nav-link abs" style="left:473px;top:30px">CONTACTS</span>
  </nav>
  <div class="logo-box abs"><span>Merido</span></div>

  <div class="hero abs" role="img" aria-label="Coffee cup with beans, bartender pouring cocktails, red wine glass with grapes and bottle"></div>
  <svg class="arrow abs" style="left:18px" viewBox="0 0 8 26"><path d="M7 1 1 13 7 25" fill="none" stroke="rgba(255,255,255,.5)" stroke-width="1.5"/></svg>
  <svg class="arrow abs" style="left:524px" viewBox="0 0 8 26"><path d="M1 1 7 13 1 25" fill="none" stroke="rgba(255,255,255,.5)" stroke-width="1.5"/></svg>
  <span class="hero-dot abs" style="left:262px;background:var(--orange)"></span>
  <span class="hero-dot abs" style="left:271px;background:#a35a10"></span>
  <span class="hero-dot abs" style="left:280px;background:#a35a10"></span>

  <section>
    <h2 class="welcome-title abs cond">WELCOME TO OUR</h2>
    <div class="welcome-rule abs"></div>
    <p class="welcome-text abs" style="top:370px">Meridoro is the process that slowly and gradually releases the purest of essence. As tea leaves unravel and coffee patiently drips, it is the best representation of the making of tea and coffee. We want the tea and coffee from Meridoro to express their many levels of character through a thoughtful and caring hand.</p>
    <p class="welcome-text abs" style="top:421px">Meridoro is a concept that we wish to pass forward. Meridoro means a healthy and positive outlook for the adopters of this great attitude.</p>
    <div class="welcome-photo abs" role="img" aria-label="Glass of white wine on a barrel among vine leaves and grapes"></div>
  </section>

  <section>
    <div class="banner abs" role="img" aria-label="Wine bottle, glass of white wine, green grapes, straw and rustic bread in a basket"></div>
    <h2 class="banner-text abs">LOREM IPSUM DOLOR SIT AMET<br>ADIPISCING ELIT SED AT</h2>
    <div class="btn-order abs">ORDER NAW</div>
  </section>

  <section>
    <div class="tab-active abs">BREKFAST</div>
    <span class="tab abs" style="left:126px">LUNCH</span>
    <span class="tab abs" style="left:179px">HAPPYHOURE</span>
    <span class="tab abs" style="left:261px">COFFEE</span>
    <span class="tab abs" style="left:323px">ROASTERY</span>
    <span class="tab abs" style="left:405px">WINEBAR</span>

    <div class="card abs" style="left:44px">
      <div class="card-photo" role="img" aria-label="Bottle and glass of red wine" style="background:radial-gradient(ellipse,#5a1418 0%,#2a0a0c 35%,#fff 70%)"></div>
      <span class="card-name">Lorem ipsum dolo</span><span class="card-price">$12.00</span>
    </div>
    <div class="card abs" style="left:211px">
      <div class="card-photo" role="img" aria-label="Cup of coffee on a saucer with coffee beans" style="background:radial-gradient(ellipse,#5b3a22 0%,#e9e4df 45%,#fff 70%)"></div>
      <span class="card-name">Lorem ipsum dolo</span><span class="card-price">$12.00</span>
    </div>
    <div class="card abs" style="left:373px">
      <div class="card-photo" role="img" aria-label="Basket of assorted breads and pastries" style="background:radial-gradient(ellipse,#c98a45 0%,#e0b27a 40%,#fff 72%)"></div>
      <span class="card-name">Lorem ipsum dolo</span><span class="card-price">$12.00</span>
    </div>
  </section>

  <section>
    <div class="video-band abs"></div>
    <h3 class="video-title abs">Do you want to retation the video recipe?</h3>
    <p class="video-text abs">Coffee is a ritual, a small treat in the morning, “fuel”, a break, chat, affair that makes up our lives. Making the coffee better, we make our lives better.</p>
    <div class="video-photo abs" role="img" aria-label="Pile of bread rolls and pastries"></div>
    <div class="video-reflect abs"></div>
    <div class="thumb abs" style="left:333px" role="img" aria-label="Video thumbnail of coffee cups"><span class="thumb-title">Coffee Around The...</span><span class="play"></span></div>
    <div class="thumb abs" style="left:425px" role="img" aria-label="Video thumbnail of a hot drink"><span class="thumb-title">Harbor Brew Hot Be...</span><span class="play"></span></div>
    <p class="thumb-cap abs" style="left:333px">Gather more knowledge from coffee</p>
    <p class="thumb-cap abs" style="left:425px">Work with green and roasted coffee provides</p>
  </section>

  <section>
    <div class="kit-photo abs" role="img" aria-label="Blue coffee cups with meringue cookies on a wooden table"></div>
    <h3 class="kit-title abs cond">GET YOUR BUTTERLIGHT COFFEE MAKING KIT</h3>
    <ul class="kit-list abs">
      <li>1 cup unsweetened cocoa powder</li>
      <li>1/2 cup butter, cut into 1-inch pieces</li>
      <li>1 1/4 cups granulated sugar</li>
      <li>1/2 cup firmly packed dark brown sugar</li>
      <li>1 1/4 tsp baking soda</li>
      <li>Add a Tidewell Insulated Coffee Flask / Shaker &amp; a Cafe Cap</li>
    </ul>
    <p class="kit-quote abs">“THE EASIEST AND MOST CONVENIENT WAY I HAVE USED IN MAKING BUTTERLIGHT COFFEE. WE USE IT VERY DAY.”</p>
  </section>

  <footer>
    <div class="site-footer abs"></div>
    <h4 class="foot-head abs cond" style="left:43px">ABOUT US</h4>
    <h4 class="foot-head abs cond" style="left:162px">FOR BUSINESS</h4>
    <h4 class="foot-head abs cond" style="left:282px">NEWSLETTER</h4>
    <h4 class="foot-head abs cond" style="left:401px">FOLLOW US</h4>

    <p class="foot-text abs" style="left:43px;top:1377px;width:110px">Anim pariatur cliche reprehenderit, enim eiusmod high life accusamus tomas rendell ad squid.</p>
    <div class="contact-row abs" style="top:1412px">
      <svg width="9" height="7" viewBox="0 0 9 7"><rect width="9" height="7" fill="#555"/><path d="M0 0 4.5 4 9 0" fill="none" stroke="#efe6da" stroke-width=".8"/></svg>
      <span class="foot-text">hello@meridocafe.com</span>
    </div>
    <div class="contact-row abs" style="top:1430px">
      <svg width="8" height="8" viewBox="0 0 8 8"><path d="M1 1c1-1 2 0 2.5 1.5L2.8 3.3c.5 1 1 1.5 2 2l.8-.7C7 5 8 6 7 7 5 8 0 3 1 1z" fill="#555"/></svg>
      <span class="foot-text">+(954)555-0147</span>
    </div>
    <div class="contact-row abs" style="top:1448px">
      <svg width="9" height="8" viewBox="0 0 9 8"><path d="M4.5 0 9 4H7.8v4H5.5V5.5h-2V8H1.2V4H0z" fill="#555"/></svg>
      <span class="foot-text">412 Harbor Lane, Suite 18<br>Fort Lauderdale FL 33301</span>
    </div>

    <p class="foot-text abs" style="left:162px;top:1377px">Office Coffee<br>Food Service<br>Affiliate Program</p>

    <p class="foot-text abs" style="left:282px;top:1377px;width:108px">If you world like sign-up to the Merido newsletter,please enter your email address below</p>
    <div class="field abs" style="top:1408px">Name</div>
    <div class="field abs" style="top:1425px">Email</div>
    <div class="btn-sub abs">SUBSCRIBE</div>

    <p class="foot-text abs" style="left:401px;top:1377px;width:110px">Follow Merido on the following social network sites.</p>
    <span class="social abs" style="left:401px;background:var(--orange)"></span>
    <span class="social abs" style="left:417px"></span>
    <span class="social abs" style="left:433px"></span>
    <span class="social abs" style="left:449px"></span>

    <div class="copy-rule abs"></div>
    <p class="copyright abs">Copyright © . All Rights Reserved</p>
  </footer>

</div>
</body>
</html>
```